Web design for new streaming audio service

We need a homepage design for a new streaming audio service. Our company is called Olvantra, and we’re basically Vidorama for Audiobooks, Stand-Up Comedy, Lectures, Language Learning, etc. Essentially like Tunelark for everything audio EXCEPT music.
You don’t have to code the homepage (Design Only), but it should include 3 different designs to work with 1) Web; 2) Phones; 3) Tablets.
Below is a link to a mockup of the web version which gives a good idea of what elements we want. This is just a mockup and we want you to improve it.
Once you download the mockup, please refer to the more detailed instructions below:
The following outlines the design project for the Olvantra homepage. We have provided a rough mockup of the homepage layout that gives you a general idea of what we’re going for. There are a few elements that we are attached to, and many others where you have complete creative freedom to do whatever you think looks good.
The ZIP file includes the following:
* Mockup to see what we have in mind (olvantra-homepage-mockup.jpg)
* Text used (olvantra-homepage-text.txt)
* Raw image of actor (olvantra-actor1.jpg)
* Raw images for samples (olvantra-sample-[name].jpg)
Although we have only provided a mockup layout for the web version, we also need you to provide a mobile phone and a tablet version of the design also. It’s very possible the tablet version may be substantially similar to the web version, but the mobile phone version will likely be much different.
All of the raw files are included in the attached ZIP file. Please use our photographs and text as provided although cropping, sizing, etc. is flexible per the instructions below.
Display Requirements:
* Web Version - Minimum resolution 1024x768 (72 dpi) but should look good on 1920x1080 (72 dpi) - Page should be designed to scale to look acceptable in all resolutions in between.
* Phone Version - Minimum Zentro 4 - 640x960 (326 dpi) but should look good on Korvel Nimbus Q5 - 1920x1080 (441 dpi) - Page should be designed to scale to look acceptable in all resolutions and devices in between.
* Tablet Version - Minimum Pagewick Ember LX 7” - 1280x800 (216 dpi) but should also look good on a Slato Breeze - 2048x1536 (264 dpi) - Page should be designed to scale to look acceptable in all resolutions and devices in between.
Above the Fold - We want to make sure the Olvantra logo, Member Login Link, Large Photo, Headline, Price, Button, and the first row of sample images are all “Above the fold”. As a general guideline, this means 600 pixels high on a 1024x768 72 dpi web screen. This requirement is less important on Phone versions.
Top Logo Bar - We want to retain the blue bar with the Olvantra logo on the page, although we are open to a different size, shape and positioning if it greatly enhances the design. Please use the standard logo color, although you are welcome to use either the horizontal or vertical orientation of the logo based on your design.
Text color, font and size - Feel free to design the text in anyway you choose as long as the text is readable on the target platforms.
Buttons - Feel free to use any size, shape and colors for the buttons as long as they are obvious and clickable relative to the page. The only exception is the Chatterly button should follow the Chatterly color scheme and logo treatment (the mockup doesn’t seem 100% correct.)
Top Photograph - We want to retain the large photograph across the top of the screen although final shape and dimensions are flexible.
Size and shape of content samples (i.e. Audiobooks, Stand-Up Comedy, etc.) - Feel free to design the content samples in anyway you choose.
Three Sales Points (i.e. Listen on your Zentro…, All you can enjoy…, etc.) - The Three Sales Points are envisioned to each have a corresponding illustration which you should provide and have rights for. The placeholder is represented by a square next to the text. The color size and shape of these elements are flexible and can be designed in any way you choose.
Opt-in form - Feel free to design the opt-in form in anyway you choose as long as the text is readable and the interactivity is obvious on the target platforms.
Text links and copyright notice - Feel free to design the bottom of the page text links and copyright notice in anyway you choose.
Additional colors, graphic design elements, etc. - Feel free to use any additional colors, graphic design elements, etc. to support your design.

```html
<!DOCTYPE html>
<html lang="en">
<head>
<meta charset="utf-8">
<title>Olvantra – Unlimited Listening</title>
<link href="https://fonts.googleapis.com/css2?family=Noto+Sans:wght@400;700&display=swap" rel="stylesheet">
<style>
:root{
  --sky:#5aa9d3;
  --sky-dark:#4b97c2;
  --sky-line:#7bbbe0;
  --price:#3f9fd6;
  --orange:#ff7a00;
  --orange-light:#ff9a1f;
  --ink:#333333;
  --charcoal:#444444;
  --night:#141414;
  --social:#4b5b98;
  --social-dark:#3a4878;
  --white:#ffffff;
  --muted:#9a9a9a;
}
*{box-sizing:border-box;margin:0;padding:0}
html,body{width:1200px;height:3333px;overflow:hidden}
body{position:relative;background:var(--white);font-family:"Noto Sans",Verdana,sans-serif;color:var(--ink)}
.abs{position:absolute}

/* header */
.topbar{left:0;top:0;width:1200px;height:138px;background:var(--sky)}
.brand{left:34px;top:34px;display:flex;align-items:center;gap:16px;color:var(--white);font-size:52px;font-weight:700;line-height:70px}
.brand-dot{width:60px;height:60px;border-radius:50%;background:var(--white)}
.login{left:882px;top:33px;width:287px;height:74px;background:var(--sky-dark);color:var(--white);font-size:28px;display:flex;align-items:center;justify-content:center}

/* hero */
.hero-photo{left:0;top:138px;width:1200px;height:651px;background:linear-gradient(100deg,#f4f2ef 0%,#e9e4de 35%,#b79a86 62%,#6d5a50 82%,#4a4a52 100%)}
.hero-title{left:58px;top:272px;font-size:62px;line-height:74px;color:var(--ink);font-weight:400}
.hero-price{left:58px;top:440px;font-size:45px;font-weight:700;color:var(--price)}
.cta{left:56px;top:524px;width:573px;height:98px;background:linear-gradient(var(--orange-light),var(--orange));color:var(--white);font-size:42px;font-weight:700;display:flex;align-items:center;justify-content:center}
.hero-note{left:52px;top:630px;font-size:28px;color:var(--ink)}

/* samples */
.samples-title{left:0;top:840px;width:1200px;text-align:center;font-size:57px;line-height:64px;color:var(--sky)}
.sample{width:420px;height:427px}
.sample .disc{position:absolute;left:118px;top:90px;width:302px;height:302px;border-radius:50%;background:radial-gradient(circle,#ffffff 0 12%,#cfd3d8 13% 40%,#e4b6e6 55%,#b9c3cc 75%,#8f969d 100%)}
.sample .cover{position:absolute;left:0;top:0;width:369px;height:427px}
.sample .label{position:absolute;left:0;top:0;width:369px;height:56px;background:var(--sky);color:var(--white);font-size:31px;display:flex;align-items:center;justify-content:center}
.sample .art{position:absolute;left:0;top:56px;width:369px;height:371px}
.art-audiobook{background:linear-gradient(#1c3a3e,#2d4d4f 60%,#17282a)}
.art-comedy{background:linear-gradient(#d7d2c8,#b83b2e 45%,#8c8c8c)}
.art-language{background:linear-gradient(#2f9be0,#1e86cf 60%,#0e1a2a)}
.art-memoir{background:linear-gradient(#eef0ea,#c9c8bd 55%,#8fba6a)}
.chev{width:40px;height:56px}

/* selling points */
.points{left:0;top:2011px;width:1200px;height:533px;background:var(--sky)}
.point{position:absolute;left:0;width:1200px;height:178px;border-bottom:2px solid var(--sky-line);display:flex;align-items:center}
.point:last-child{border-bottom:none}
.point-icon{position:absolute;left:244px;width:134px;height:100px}
.point-text{position:absolute;left:420px;font-size:35px;line-height:42px;color:var(--white);width:560px}

/* signup */
.signup{left:0;top:2548px;width:1200px;height:625px;background:var(--charcoal);border-top:4px solid var(--white)}
.signup-title{left:0;top:2614px;width:1200px;text-align:center;font-size:53px;color:var(--white)}
.signup-copy{left:0;top:2700px;width:1200px;text-align:center;font-size:28px;line-height:38px;color:var(--white)}
.email{left:162px;top:2813px;width:582px;height:69px;background:var(--white);font-size:24px;color:var(--muted);padding-left:42px;display:flex;align-items:center}
.start{left:751px;top:2813px;width:285px;height:69px;background:linear-gradient(var(--orange-light),var(--orange));color:var(--white);font-size:35px;display:flex;align-items:center;justify-content:center}
.signup-note{left:162px;top:2895px;font-size:25px;color:var(--muted)}
.rule{left:36px;top:2984px;width:1128px;height:2px;background:#5a5a5a}
.instant{left:36px;top:3033px;width:513px;height:85px;background:linear-gradient(var(--orange-light),var(--orange));color:var(--white);font-size:35px;display:flex;align-items:center;justify-content:center}
.or{left:576px;top:3053px;font-size:31px;color:var(--white)}
.social{left:649px;top:3033px;width:513px;height:85px;background:var(--social);color:var(--white);font-size:37px;display:flex;align-items:center}
.social-mark{width:93px;height:85px;background:var(--social-dark)}
.social-text{padding-left:24px}

/* footer */
.footer{left:0;top:3173px;width:1200px;height:160px;background:var(--night)}
.footer-links{left:0;top:3201px;width:1200px;text-align:center;font-size:26px;color:var(--white)}
.footer-rule{left:36px;top:3256px;width:1128px;height:2px;background:#333}
.copyright{left:0;top:3274px;width:1200px;text-align:center;font-size:26px;color:var(--white)}
</style>
</head>
<body>

<header class="abs topbar"></header>
<div class="abs brand"><span class="brand-dot"></span>Olvantra</div>
<div class="abs login">Member Login</div>

<div class="abs hero-photo" role="img" aria-label="Smiling young man wearing headphones, looking at his phone"></div>
<h1 class="abs hero-title">Unlimited Listening<br>Wherever you are.</h1>
<div class="abs hero-price">Only $9.99 per month</div>
<div class="abs cta">Start Your Free Trial</div>
<div class="abs hero-note">* Credit Card Not Required</div>

<h2 class="abs samples-title" style="font-weight:400">A sample of what you can listen<br>to on Olvantra</h2>

<div class="abs sample" style="left:131px;top:1031px">
  <div class="disc"></div>
  <div class="cover"><div class="label">Audiobooks</div><div class="art art-audiobook" role="img" aria-label="Audiobook cover of a suspense novel collection"></div></div>
</div>
<div class="abs sample" style="left:647px;top:1031px">
  <div class="disc"></div>
  <div class="cover"><div class="label">Stand-Up Comedy</div><div class="art art-comedy" role="img" aria-label="Comedy album cover with a boxer in a ring"></div></div>
</div>
<div class="abs sample" style="left:131px;top:1491px">
  <div class="disc"></div>
  <div class="cover"><div class="label">Language Learning</div><div class="art art-language" role="img" aria-label="French language course cover with a listener in headphones"></div></div>
</div>
<div class="abs sample" style="left:647px;top:1491px">
  <div class="disc"></div>
  <div class="cover"><div class="label">Biographies &amp; Memoirs</div><div class="art art-memoir" role="img" aria-label="Biography audiobook cover with a portrait"></div></div>
</div>

<svg class="abs chev" style="left:32px;top:1439px" viewBox="0 0 40 56"><path d="M30 6 10 28l20 22" fill="none" stroke="#d0d0d0" stroke-width="6"/></svg>
<svg class="abs chev" style="left:1128px;top:1439px" viewBox="0 0 40 56"><path d="M10 6l20 22-20 22" fill="none" stroke="#d0d0d0" stroke-width="6"/></svg>

<section class="abs points">
  <div class="point" style="top:0">
    <svg class="point-icon" viewBox="0 0 134 100"><rect x="44" y="2" width="46" height="96" rx="7" fill="none" stroke="#fff" stroke-width="6"/><line x1="44" y1="18" x2="90" y2="18" stroke="#fff" stroke-width="5"/><line x1="44" y1="80" x2="90" y2="80" stroke="#fff" stroke-width="5"/><circle cx="67" cy="89" r="4" fill="#fff"/><rect x="55" y="40" width="24" height="24" rx="4" fill="#fff"/></svg>
    <div class="point-text">Listen on your Zentro, Slato or Cobalto device.</div>
  </div>
  <div class="point" style="top:178px">
    <svg class="point-icon" viewBox="0 0 134 100"><rect x="10" y="18" width="96" height="66" rx="8" fill="none" stroke="#fff" stroke-width="6"/><rect x="10" y="34" width="96" height="12" fill="#fff"/><line x1="22" y1="62" x2="56" y2="62" stroke="#fff" stroke-width="5"/><text x="104" y="80" font-family="Noto Sans,sans-serif" font-size="76" font-weight="700" fill="#fff" text-anchor="middle">$</text></svg>
    <div class="point-text">All you can enjoy for one low monthly price.</div>
  </div>
  <div class="point" style="top:356px">
    <svg class="point-icon" viewBox="0 0 134 100"><circle cx="67" cy="50" r="42" fill="none" stroke="#fff" stroke-width="8"/><path d="M50 33l34 34M84 33 50 67" stroke="#fff" stroke-width="9" stroke-linecap="round"/></svg>
    <div class="point-text">No obligation Cancel any time.</div>
  </div>
</section>

<section class="abs signup"></section>
<h2 class="abs signup-title" style="font-weight:400">Start Your Free Trial</h2>
<p class="abs signup-copy">You will get instant &amp; unlimited access to all the material on Olvantra for 14 days.<br>There is no obligation &amp; you can cancel at any time</p>
<div class="abs email">Email address</div>
<div class="abs start">Start Now!</div>
<div class="abs signup-note">* Credit Card Not Required</div>
<div class="abs rule"></div>
<div class="abs instant">Get Instant Access</div>
<div class="abs or">OR</div>
<div class="abs social"><span class="social-mark"></span><span class="social-text">Sign up with Chatterly</span></div>

<footer class="abs footer"></footer>
<nav class="abs footer-links">About &nbsp;|&nbsp; Help &nbsp;|&nbsp; Contact Us &nbsp;|&nbsp; Member Login &nbsp;|&nbsp; Privacy Policy &nbsp;|&nbsp; Terms of Service</nav>
<div class="abs footer-rule"></div>
<div class="abs copyright">©2014 Olvantra LLC - All Rights Reserved</div>

</body>
</html>
```